Quality Monitoring Company Needs a New Site

We are an established company that has a fair number of clients but the site lacks current design standards that we'd like to keep up with. We'd like to mimic the same style of the site on quillorbit.example, vemora.example, https://tandrelfunds.example/, etc. We'd also like to make sure the designer understands SEO Silos and how it effects the design elements. Attached is the structure that I'd like to follow for the pages. You don't need to design every single sub-page because they'll probably be fairly similar; however, I want to see at least 1 each. Please use the content on our current site for filler areas. Please try to do a good job of understanding what we do so you can use your best judgement on what is needed to be successful. Use our color scheme and the logo should be the side view but I included the AI just in case.
Updates

I am narrowing down on the field of designs that I have received. There are a lot of similarities between the designs I like and don't like. I'd also like to ensure that some of the inner pages get done in the next 5 days so I can see the creativity that is there as well. That is probably what is next -- getting a few inner pages completed so I can see what you can come up with (not based on our current website) because the current "front pages" are all so good and so close.

Industry/Entity Type

Telecommunications

Colors

Designer to choose colors to be used in the design.

Requirements
Must have
• SEO Silo Look and Feel
• Current Colors
Should not have
• No stockphotos whatsoever. NONE.

```html
<!DOCTYPE html>
<html lang="en">
<head>
<meta charset="utf-8">
<title>Vocalyst – AI Enabled Voice Analytics</title>
<link href="https://fonts.googleapis.com/css2?family=Poppins:wght@300;400;500;600;700&display=swap" rel="stylesheet">
<style>
:root{
  --navy:#002d5a;
  --sky:#06b2e6;
  --page:#f5f7fb;
  --text:#4a4f5c;
  --white:#ffffff;
  --rule:#1d4a75;
}
*{margin:0;padding:0;box-sizing:border-box}
html,body{width:1200px;height:1180px;overflow:hidden}
body{font-family:'Poppins',sans-serif;background:var(--page);position:relative;color:var(--text)}
.abs{position:absolute}
.hero-blob{left:700px;top:0;width:520px;height:612px;background:#eceff7;border-radius:0 0 0 520px/0 0 0 612px;clip-path:ellipse(75% 100% at 100% 0%)}
.brand{left:139px;top:58px;display:flex;align-items:center;gap:8px;font-size:20px;font-weight:600;color:var(--navy)}
.brand-dot{width:18px;height:18px;border-radius:50%;background:var(--sky)}
.nav{left:404px;top:78px;display:flex;font-size:12px;color:#2b2f3a}
.nav a{position:absolute;white-space:nowrap;text-decoration:none;color:inherit}
.nav .active{color:var(--sky);font-weight:600}
.phone{left:903px;top:64px;display:flex;align-items:center;gap:10px}
.phone-badge{width:38px;height:38px;border-radius:50%;background:var(--sky);display:flex;align-items:center;justify-content:center}
.phone-num{font-size:14px;font-weight:700;color:var(--navy);letter-spacing:.3px}
.dropdown{left:443px;top:102px;width:191px;height:133px;background:var(--white);box-shadow:0 6px 18px rgba(0,30,70,.08);z-index:3}
.dropdown span{position:absolute;left:18px;font-size:11.3px;color:#555b66}
.dropdown .current{left:7px;top:94px;width:177px;height:28px;background:var(--sky);color:var(--white);font-weight:500;display:flex;align-items:center;padding-left:11px;border-radius:2px}
.hero-title{left:142px;top:190px;font-size:28px;font-weight:700;color:var(--navy);white-space:nowrap}
.hero-title em{font-style:normal;font-weight:500;color:var(--sky)}
.hero-rule{left:140px;top:239px;width:36px;height:2px;background:var(--sky)}
.hero-copy{left:143px;width:460px;font-size:11.3px;line-height:19px}
.checks{left:142px;top:432px;list-style:none;font-size:11.3px}
.checks li{height:32.3px;display:flex;align-items:flex-start;gap:11px}
.showcase{left:664px;top:178px;width:484px;height:426px;border-radius:8px;background:linear-gradient(160deg,#dfe9f0 0%,#b9d9ea 55%,#2f4a78 100%)}
.band{left:0;top:806px;width:1200px;height:374px;background:var(--navy)}
.shout{left:211px;top:701px;width:777px;height:211px;border-radius:106px;background:var(--sky);text-align:center}
.shout h2{font-size:44px;font-weight:300;color:var(--white);margin-top:48px;letter-spacing:1px}
.shout a{display:inline-block;margin-top:18px;width:155px;height:35px;line-height:35px;border-radius:18px;background:var(--navy);color:var(--white);font-size:13px;text-decoration:none}
.foot-h{top:967px;font-size:17px;font-weight:700;color:var(--sky)}
.foot-links a{position:absolute;font-size:11.5px;color:var(--white);text-decoration:none;white-space:nowrap}
.contact-line{font-size:12.5px;color:var(--white);line-height:23px;white-space:nowrap}
.foot-mark{left:940px;top:970px;display:flex;align-items:center;gap:10px;font-size:20px;font-weight:600;color:var(--white)}
.foot-mark i{width:22px;height:22px;border-radius:50%;background:var(--sky);display:block}
.foot-rule{left:139px;top:1133px;width:919px;height:1px;background:var(--rule)}
.copy{left:0;top:1147px;width:1200px;text-align:center;font-size:12px;color:var(--white)}
</style>
</head>
<body>
<div class="abs hero-blob"></div>

<div class="abs brand"><span class="brand-dot"></span>Vocalyst</div>

<nav class="abs nav">
  <a style="left:0">Home</a>
  <a class="active" style="left:59px">Services</a>
  <a style="left:133px">Industries</a>
  <a style="left:216px">Pricing</a>
  <a style="left:279px">Team</a>
  <a style="left:338px">Blog</a>
  <a style="left:389px">Contact Us</a>
</nav>

<div class="abs phone">
  <div class="phone-badge">
    <svg width="16" height="16" viewBox="0 0 24 24"><path fill="#fff" d="M6.6 10.8a15.1 15.1 0 0 0 6.6 6.6l2.2-2.2c.3-.3.7-.4 1-.2 1.1.4 2.3.6 3.6.6.6 0 1 .4 1 1V20c0 .6-.4 1-1 1A17 17 0 0 1 3 4c0-.6.4-1 1-1h3.5c.6 0 1 .4 1 1 0 1.3.2 2.5.6 3.6.1.3 0 .7-.2 1z"/></svg>
  </div>
  <span class="phone-num">555-014-2290</span>
</div>

<div class="abs dropdown">
  <span style="top:11px">Quality Assurance</span>
  <span style="top:38px">Coaching</span>
  <span style="top:64px">Sales Performance</span>
  <span class="current">AI Enabled Voice Analytics</span>
</div>

<h1 class="abs hero-title">AI Enabled <em>Voice Analytics</em></h1>
<div class="abs hero-rule"></div>

<p class="abs hero-copy" style="top:259px">Lorem ipsum dolor sit amet, consectetuer adipiscing elit, sed diam nonummy nibh euismod tincidunt ut laoreet dolore magna aliquam erat volutpat. Ut wisi enim ad minim veniam, quis nostrud exerci tation ullamcorper suscipit lobortis nisl ut aliquip exea commodo consequat.</p>
<p class="abs hero-copy" style="top:356px">Lorem ipsum dolor sit amet, consectetuer adipiscing elit, sed diam nonummy nibh euismod tincidunt ut laoreet dolore magna aliquam erat volutpat. Ut wisi enim ad minim veniam, quis nostrud exerci tation</p>

<ul class="abs checks">
  <li><svg width="11" height="11" viewBox="0 0 12 12" style="margin-top:4px"><path d="M1.5 6.5l3 3 6-7" fill="none" stroke="#06b2e6" stroke-width="2"/></svg>Consectetuer adipiscing elit sed diam nonummy</li>
  <li><svg width="11" height="11" viewBox="0 0 12 12" style="margin-top:4px"><path d="M1.5 6.5l3 3 6-7" fill="none" stroke="#06b2e6" stroke-width="2"/></svg>Nibh euismod tincidunt ut laoreet dolore magna</li>
  <li><svg width="11" height="11" viewBox="0 0 12 12" style="margin-top:4px"><path d="M1.5 6.5l3 3 6-7" fill="none" stroke="#06b2e6" stroke-width="2"/></svg>Aliquam erat volutpat. Ut wisi enim ad minim veniam</li>
  <li><svg width="11" height="11" viewBox="0 0 12 12" style="margin-top:4px"><path d="M1.5 6.5l3 3 6-7" fill="none" stroke="#06b2e6" stroke-width="2"/></svg>Quis nostrud exerci tation ullamcorper suscipit lobortis</li>
</ul>

<div class="abs showcase" role="img" aria-label="Illustration of two people working in front of a large analytics dashboard with profile, feed, contact and calendar panels"></div>

<div class="abs band"></div>

<section class="abs shout">
  <h2>Give Us A Shout</h2>
  <a>GET IN TOUCH</a>
</section>

<h3 class="abs foot-h" style="left:139px">Quick Links</h3>
<div class="foot-links">
  <a class="abs" style="left:139px;top:1003px">Home</a>
  <a class="abs" style="left:139px;top:1023px">Services</a>
  <a class="abs" style="left:139px;top:1043px">System Details</a>
  <a class="abs" style="left:139px;top:1064px">Pricing</a>
  <a class="abs" style="left:294px;top:1003px">Team</a>
  <a class="abs" style="left:294px;top:1023px">Blog</a>
  <a class="abs" style="left:294px;top:1043px">Contact Us</a>
  <a class="abs" style="left:294px;top:1064px">Login</a>
</div>

<h3 class="abs foot-h" style="left:460px">Contact Us</h3>
<svg class="abs" style="left:462px;top:1008px" width="11" height="15" viewBox="0 0 12 16"><path fill="#fff" d="M6 0a6 6 0 0 0-6 6c0 4.5 6 10 6 10s6-5.5 6-10a6 6 0 0 0-6-6zm0 8.3A2.3 2.3 0 1 1 6 3.7a2.3 2.3 0 0 1 0 4.6z"/></svg>
<div class="abs contact-line" style="left:480px;top:1002px">4810 Harbor Crest Blvd.<br>Westvale, CA 90000</div>
<svg class="abs" style="left:660px;top:1008px" width="14" height="14" viewBox="0 0 24 24"><path fill="#fff" d="M6.6 10.8a15.1 15.1 0 0 0 6.6 6.6l2.2-2.2c.3-.3.7-.4 1-.2 1.1.4 2.3.6 3.6.6.6 0 1 .4 1 1V20c0 .6-.4 1-1 1A17 17 0 0 1 3 4c0-.6.4-1 1-1h3.5c.6 0 1 .4 1 1 0 1.3.2 2.5.6 3.6.1.3 0 .7-.2 1z"/></svg>
<div class="abs contact-line" style="left:682px;top:1002px">555-014-2290</div>
<svg class="abs" style="left:660px;top:1045px" width="15" height="11" viewBox="0 0 16 12"><rect width="16" height="12" rx="1.5" fill="#fff"/><path d="M1 1.5l7 5 7-5" fill="none" stroke="#002d5a" stroke-width="1.4"/></svg>
<div class="abs contact-line" style="left:682px;top:1038px">hello@vocalyst.example</div>

<div class="abs foot-mark"><i></i>Vocalyst</div>

<div class="abs foot-rule"></div>
<p class="abs copy">Copyright © 2019 VOCALYST. All Rights Reserved.</p>
</body>
</html>
```